Business Card Redesign

We would like to redesign our existing business cards.
The new design shall look:
ELEGANT, LUXURY, PROFESSIONAL
Reference:
YOU CAN VISIT WWW.LUMEN-RIVET.HK FOR BETTER UNDERSTANDING OF COMPANY STRATEGY AND POSITION
Additional:
CHOSEN CANDIDATE SHALL PROVIDE THE INSTRUCTION OF PRINTING IF ANY THERMAL COVERAGE OR ANY ADDITION IS OFFERED
Industry/Entity Type
Business

```html
<!DOCTYPE html>
<html lang="en">
<head>
<meta charset="utf-8">
<title>Lumen Rivet Limited — Business Cards</title>
<link href="https://fonts.googleapis.com/css2?family=Noto+Sans:wght@400;600&family=Noto+Sans+TC:wght@400;500&display=swap" rel="stylesheet">
<style>
  :root {
    --page: #ecebe7;
    --card: #cbc6ba;
    --band: #5d3e20;
    --band-text: #f1e9dc;
    --ink: #3b3733;
    --link: #23428f;
    --seal: #c49a2c;
    --seal-ring: #1f3a7a;
  }
  * { margin: 0; padding: 0; box-sizing: border-box; }
  html, body { width: 1200px; height: 900px; overflow: hidden; }
  body {
    background: var(--page);
    font-family: "Noto Sans", "Noto Sans TC", sans-serif;
    color: var(--ink);
    display: flex;
    align-items: center;
    justify-content: center;
    gap: 40px;
  }
  .card {
    position: relative;
    width: 520px;
    height: 312px;
    background: var(--card);
    box-shadow: 0 6px 18px rgba(0,0,0,0.18);
    overflow: hidden;
  }
  .card__band {
    position: absolute;
    left: 0; right: 0;
    top: 44px;
    height: 66px;
    background: var(--band);
  }
  .brand {
    position: absolute;
    left: 26px;
    top: 42px;
    display: flex;
    align-items: center;
    gap: 10px;
  }
  .brand__seal {
    width: 70px; height: 70px;
    border-radius: 50%;
    background: var(--seal);
    border: 5px solid var(--seal-ring);
  }
  .brand__name {
    font-size: 13px;
    font-weight: 600;
    letter-spacing: 0.08em;
    color: var(--band-text);
  }
  .person {
    position: absolute;
    left: 300px;
    top: 50px;
    color: var(--band-text);
    line-height: 1.25;
  }
  .person__name { font-size: 17px; font-weight: 600; letter-spacing: 0.03em; }
  .person__title { font-size: 11px; margin-bottom: 2px; }
  .person__line { font-size: 10px; }
  .contact {
    position: absolute;
    left: 300px;
    top: 128px;
    font-size: 10.5px;
    line-height: 1.45;
  }
  .contact__web { color: var(--link); }
  .address {
    position: absolute;
    left: 34px;
    top: 176px;
    font-size: 12.5px;
    line-height: 1.4;
  }
  .address__label { margin-bottom: 14px; letter-spacing: 0.02em; }
  .card--zh .person__name { font-size: 16px; font-weight: 500; letter-spacing: 0.12em; }
  .card--zh { font-family: "Noto Sans TC", "Noto Sans", sans-serif; }
</style>
</head>
<body>
  <section class="card card--zh" lang="zh-Hant">
    <div class="card__band"></div>
    <div class="brand">
      <div class="brand__seal"></div>
      <span class="brand__name">LUMEN RIVET LIMITED</span>
    </div>
    <div class="person">
      <div class="person__name">林可澄</div>
      <div class="person__title">公關顧問</div>
      <div class="person__line">電郵 dana@lumen-rivet.hk</div>
      <div class="person__line">手提 (852) 6417 2085</div>
    </div>
    <div class="contact">
      <div>電話 (852) 2740-3318</div>
      <div>傳真 (852) 2740-3319</div>
      <div class="contact__web">www.lumen-rivet.hk</div>
    </div>
    <div class="address">
      <div class="address__label">香港總部</div>
      <div>香港中環燈籠街18號</div>
      <div>港灣中心12樓1201B</div>
    </div>
  </section>

  <section class="card card--en">
    <div class="card__band"></div>
    <div class="brand">
      <div class="brand__seal"></div>
      <span class="brand__name">LUMEN RIVET LIMITED</span>
    </div>
    <div class="person">
      <div class="person__name">DANA LOWE</div>
      <div class="person__title">PR Consultant</div>
      <div class="person__line">E dana@lumen-rivet.hk</div>
      <div class="person__line">M (852) 6417 2085</div>
    </div>
    <div class="contact">
      <div>T (852) 2740-3318</div>
      <div>F (852) 2740-3319</div>
      <div class="contact__web">www.lumen-rivet.hk</div>
    </div>
    <div class="address">
      <div class="address__label">HEADQUARTERS (HONG KONG)</div>
      <div>Rm. 1201B, 12/F, Harbourlane Centre,</div>
      <div>18 Lantern Street, Central,</div>
      <div>Hong Kong</div>
    </div>
  </section>
</body>
</html>
```